MEDICAL OAKWELL CENTER (Medical Clinic)

Our Building is named the "Medical Oakwell Center". We are looking for signs for our 3-story medical oakwell clinic building. The signs will be located on four locations on the front building face. two signs will be placed on the middle of building ( top and above car port) and one sign on each end wing wall. we are looking for a modern font block letters, elegant, clean and eye catching fonts for the signs and a nice logo as well. it may be back-lighted signage located on the four areas of the building.

Target Market(s)

Medical patients, doctors, public. We live in the tropical island of Guam USA in the Pacific Ocean.

Industry/Entity Type

medical purpose, health facility, doctor's clinic

Colors

Designer to choose colors to be used in the design.

Requirements
Must have
• must complement the colors: Burnished Clay (neutral), Crystal Ball ( dark green), and Holly Glen ( lighther green)
Nice to have
• Back-lighted signs for the 4 areas on the building. Nice to have a logo as well.

```html
<!DOCTYPE html>
<html lang="en">
<head>
<meta charset="utf-8">
<title>Medical Oakwell Center – Sign Concepts</title>
<link rel="stylesheet" href="https://fonts.googleapis.com/css2?family=Audiowide&display=swap">
<style>
  :root {
    --deep-green: #062a2d;
    --teal: #0c4f5c;
    --white: #ffffff;
    --silver: #b8bcbd;
  }
  html, body {
    margin: 0;
    padding: 0;
    width: 1200px;
    height: 1200px;
    overflow: hidden;
    background: var(--white);
  }
  .sign-sheet {
    display: block;
    width: 1200px;
    height: 1200px;
  }
  .sign-text {
    font-family: "Audiowide", sans-serif;
    fill: var(--deep-green);
    letter-spacing: 1px;
  }
  .mark { fill: var(--deep-green); }
  .panel-frame { fill: none; stroke: var(--deep-green); stroke-width: 3; }
  .field-dark { fill: var(--deep-green); }
  .field-teal { fill: var(--teal); }
  .field-white { fill: var(--white); }
  .edge-shine { fill: none; stroke: var(--silver); stroke-width: 2; }
</style>
</head>
<body>
<svg class="sign-sheet" viewBox="0 0 1200 1200" xmlns="http://www.w3.org/2000/svg">
  <defs>
    <clipPath id="banner-clip"><rect x="0" y="0" width="1200" height="290"/></clipPath>
  </defs>

  <!-- Top facade sign -->
  <g class="sign-banner" clip-path="url(#banner-clip)">
    <rect class="field-dark" x="0" y="0" width="1200" height="290"/>
    <ellipse class="field-teal" cx="588" cy="120" rx="271" ry="228"/>
    <ellipse class="field-teal" cx="605" cy="170" rx="271" ry="228"/>
    <ellipse class="field-white" cx="596" cy="145" rx="271" ry="228"/>
    <rect class="mark" x="576" y="63" width="40" height="40" rx="8"/>
    <text class="sign-text" x="597" y="178" font-size="33" text-anchor="middle">MEDICAL OAKWELL</text>
    <text class="sign-text" x="597" y="220" font-size="33" text-anchor="middle">CENTER</text>
  </g>

  <!-- Wing wall sign (tall) -->
  <g class="sign-wing">
    <rect class="field-white" x="13" y="395" width="511" height="780"/>
    <path class="field-teal" d="M15,780 Q260,782 440,668 Q300,845 15,848 Z"/>
    <path class="field-dark" d="M15,848 Q310,842 523,538 L523,1175 L15,1175 Z"/>
    <path class="edge-shine" d="M15,846 Q310,840 440,668"/>
    <rect class="panel-frame" x="13" y="395" width="511" height="780"/>
    <rect class="mark" x="40" y="447" width="58" height="52" rx="8"/>
    <text class="sign-text" x="112" y="486" font-size="36">MEDICAL</text>
    <text class="sign-text" x="112" y="546" font-size="36">OAKWELL</text>
    <text class="sign-text" x="112" y="606" font-size="36">CENTER</text>
  </g>

  <!-- Carport sign -->
  <g class="sign-carport">
    <rect class="field-white" x="709" y="668" width="469" height="507"/>
    <path class="field-teal" d="M710,853 Q840,915 975,923 Q840,925 710,888 Z"/>
    <path class="field-dark" d="M710,888 Q850,930 975,925 Q1090,920 1177,884 L1177,1175 L710,1175 Z"/>
    <path class="edge-shine" d="M710,887 Q850,929 975,924 Q1090,919 1177,884"/>
    <rect class="panel-frame" x="709" y="668" width="469" height="507"/>
    <rect class="mark" x="925" y="741" width="36" height="36" rx="7"/>
    <text class="sign-text" x="943" y="829" font-size="25" text-anchor="middle">MEDICAL OAKWELL</text>
    <text class="sign-text" x="943" y="862" font-size="25" text-anchor="middle">CENTER</text>
  </g>
</svg>
</body>
</html>
```